Skin care manufacturer looking for packaging design for new skin care brand.

We need a design and logo for a skin care brand to be sold at retail stores and online in the United States and Europe. The design will be for 1.7oz - 2oz serums that will not have a retail box. The name of the brand is Orvia Lune and should be a luxurious brand that is approachable. The brand will consist of 4 face serums - Vitamin C, Collagen, Retinol and Hyaluronic Acid that all contain Dead Sea Minerals. Images shown are for inspiration only. Color of bottles can be varied based on design and bottles can be screen printed or labeled.

```html
<!DOCTYPE html>
<html lang="en">
<head>
<meta charset="utf-8">
<title>Orvia Lune Skin Care – Serum Labels</title>
<link rel="stylesheet" href="https://fonts.googleapis.com/css2?family=Questrial&family=Josefin+Sans:ital,wght@0,300;0,400;1,300&display=swap">
<style>
  :root {
    --paper: #ffffff;
    --teal: #00434a;
    --maroon: #4a0012;
    --navy: #0b1d47;
    --plum: #4a0046;
    --copper: #b88c6f;
    --champagne: #e8d6c2;
    --ivory: #f4ece4;
    --rule-dark: #7a5a48;
  }
  * { margin: 0; padding: 0; box-sizing: border-box; }
  html, body { width: 951px; height: 1200px; overflow: hidden; background: var(--paper); }
  body { position: relative; font-family: "Questrial", "Century Gothic", sans-serif; color: var(--ivory); }

  .brand-panel {
    position: absolute; left: 528px; top: 0; width: 423px; height: 343px;
    background: var(--teal); text-align: center;
  }
  .brand-panel .brand-dot {
    position: absolute; left: 155px; top: 67px; width: 114px; height: 114px;
    border-radius: 50%; background: var(--copper);
  }
  .brand-panel .brand-name {
    position: absolute; left: 0; right: 0; top: 190px;
    font-size: 46px; letter-spacing: 1px; color: var(--copper); line-height: 1;
  }
  .brand-panel .brand-sub {
    position: absolute; left: 0; right: 0; top: 248px;
    font-size: 21px; letter-spacing: 9px; color: var(--ivory); line-height: 1; padding-left: 9px;
  }

  .product-lineup {
    position: absolute; left: 205px; top: 428px; width: 526px; height: 360px;
    background: radial-gradient(ellipse at 50% 55%, #c9234a 0%, #6a2a52 45%, rgba(255,255,255,0) 72%);
    opacity: .35; border-radius: 12px;
  }

  .label-row {
    position: absolute; left: 49px; top: 867px; width: 847px; height: 257px;
    display: flex; gap: 9px;
  }
  .serum-label {
    position: relative; flex: 0 0 205px; height: 257px; text-align: center;
  }
  .serum-label.vitamin-c { background: var(--teal); }
  .serum-label.hyaluronic { background: var(--maroon); }
  .serum-label.retinol { background: var(--navy); }
  .serum-label.collagen { background: var(--plum); }

  .serum-label .label-dot {
    position: absolute; left: 80px; top: 14px; width: 45px; height: 45px;
    border-radius: 50%; background: var(--copper);
  }
  .serum-label .label-brand {
    position: absolute; left: 0; right: 0; top: 64px;
    font-size: 18px; color: var(--copper); line-height: 1;
  }
  .serum-label .label-sub {
    position: absolute; left: 0; right: 0; top: 85px;
    font-size: 8.5px; letter-spacing: 4px; padding-left: 4px; line-height: 1;
  }
  .serum-label .rule {
    position: absolute; left: 0; right: 0; height: 3px;
    background: linear-gradient(90deg, var(--rule-dark), var(--champagne) 50%, var(--rule-dark));
  }
  .serum-label .rule.top { top: 104px; }
  .serum-label .rule.bottom { top: 163px; }
  .serum-label .active-name {
    position: absolute; left: 0; right: 0; top: 121px;
    font-family: "Josefin Sans", sans-serif; font-weight: 300;
    font-size: 28px; color: var(--champagne); line-height: 1; white-space: nowrap;
  }
  .serum-label .active-name.long { font-size: 21px; top: 121px; }
  .serum-label .minerals {
    position: absolute; left: 0; right: 0; top: 147px;
    font-family: "Josefin Sans", sans-serif; font-style: italic; font-weight: 300;
    font-size: 8.5px; letter-spacing: .8px; line-height: 1;
  }
  .serum-label .minerals.long { top: 143px; }
  .serum-label .claim {
    position: absolute; left: 0; right: 0; top: 181px;
    font-size: 12.5px; letter-spacing: .5px; line-height: 1;
  }
  .serum-label .format {
    position: absolute; left: 0; right: 0; top: 195px;
    font-size: 15px; letter-spacing: 1px; line-height: 1;
  }
  .serum-label .benefit {
    position: absolute; left: 0; right: 0; top: 214px;
    font-size: 9px; letter-spacing: .8px; line-height: 1; white-space: nowrap;
  }
  .serum-label .tested {
    position: absolute; left: 12px; top: 243px;
    font-size: 5.5px; line-height: 1; letter-spacing: -.1px;
  }
  .serum-label .volume {
    position: absolute; right: 9px; top: 241px;
    font-size: 7px; line-height: 1;
  }
</style>
</head>
<body>
  <section class="brand-panel">
    <span class="brand-dot"></span>
    <div class="brand-name">ORVIA LUNE</div>
    <div class="brand-sub">SKIN CARE</div>
  </section>

  <div class="product-lineup" role="img" aria-label="Rendered lineup of four dropper serum bottles with gold caps wearing the teal, navy, maroon and plum labels"></div>

  <section class="label-row">
    <article class="serum-label vitamin-c">
      <span class="label-dot"></span>
      <div class="label-brand">ORVIA LUNE</div>
      <div class="label-sub">SKIN CARE</div>
      <span class="rule top"></span>
      <div class="active-name">VITAMIN C</div>
      <div class="minerals">With Dead Sea Minerals</div>
      <span class="rule bottom"></span>
      <div class="claim">ANTI-AGING</div>
      <div class="format">FACIAL SERUM</div>
      <div class="benefit">Brightening &amp; Antioxidant Defense</div>
      <div class="tested">DERMATOLOGIST TESTED</div>
      <div class="volume">1.7 oz / 50 ml</div>
    </article>

    <article class="serum-label hyaluronic">
      <span class="label-dot"></span>
      <div class="label-brand">ORVIA LUNE</div>
      <div class="label-sub">SKIN CARE</div>
      <span class="rule top"></span>
      <div class="active-name long">HYALURONIC ACID</div>
      <div class="minerals long">With Dead Sea Minerals</div>
      <span class="rule bottom"></span>
      <div class="claim">ANTI-AGING</div>
      <div class="format">FACIAL SERUM</div>
      <div class="benefit">Hydrating &amp; Plumping Formula</div>
      <div class="tested">DERMATOLOGIST TESTED</div>
      <div class="volume">1.7 oz / 50 ml</div>
    </article>

    <article class="serum-label retinol">
      <span class="label-dot"></span>
      <div class="label-brand">ORVIA LUNE</div>
      <div class="label-sub">SKIN CARE</div>
      <span class="rule top"></span>
      <div class="active-name">RETINOL</div>
      <div class="minerals">With Dead Sea Minerals</div>
      <span class="rule bottom"></span>
      <div class="claim">ANTI-AGING</div>
      <div class="format">FACIAL SERUM</div>
      <div class="benefit">Anti-Aging &amp; Smoothing Treatment</div>
      <div class="tested">DERMATOLOGIST TESTED</div>
      <div class="volume">1.7 oz / 50 ml</div>
    </article>

    <article class="serum-label collagen">
      <span class="label-dot"></span>
      <div class="label-brand">ORVIA LUNE</div>
      <div class="label-sub">SKIN CARE</div>
      <span class="rule top"></span>
      <div class="active-name">COLLAGEN</div>
      <div class="minerals">With Dead Sea Minerals</div>
      <span class="rule bottom"></span>
      <div class="claim">ANTI-AGING</div>
      <div class="format">FACIAL SERUM</div>
      <div class="benefit">Firming &amp; Revitalizing Serum</div>
      <div class="tested">DERMATOLOGIST TESTED</div>
      <div class="volume">1.7 oz / 50 ml</div>
    </article>
  </section>
</body>
</html>
```